Web design for Marketplace

Guys!
1st of all, thank you for willing to help me out.
I have attached PDF file with examples.
I am looking for professional and clean design for my new project “ Lantern of Seers “. Its marketplace for Psychic Readers around the world. Where they will able to register to provide their services via Chat,Email and sell their products on their personal stores.
Customer will able to get services and buy products from Psychic on Marketplace.
url : http://www.lanternofseers-demo.net
Please note: it doesn’t matter, what my current site looks like. I am looking for completely new design.
It doesn't matter if you add or remove : Vidlume video or even text which is on the home page in new design.
Following are the main pages of the website, which i am looking to be design.
1. Home page
2. Psychic
3. Marketplace
4. Psychic profile page
5. Psychic Store page
6. Psychic product page
7. Logo
following is the website, which i like the most. I would love to have something like that. It is neat , clean and friendly. I am looking for depth in design and neatness and borders (matter and a lot and it should be prefect ).
http://www.craftnook-demo.net
P.S : i believe it will be helpful to choose one of you. If you can only create design of " Homepage" at 1st , so i can go ahead and hire one of you guys.
Best,
Hi guys!
Guys,

```html
<!DOCTYPE html>
<html lang="en">
<head>
<meta charset="utf-8">
<title>Lantern of Seers – Home</title>
<link rel="stylesheet" href="https://fonts.googleapis.com/css2?family=Source+Sans+3:wght@400;600;700&family=Roboto+Condensed:ital,wght@1,700&display=swap">
<style>
  :root {
    --orange: #f26522;
    --orange-light: #ff8a3d;
    --red-price: #e0241b;
    --maroon: #8b1a10;
    --text: #333333;
    --muted: #555555;
    --line: #d6d6d6;
    --frame: #cfcfcf;
    --dark: #1c1c1c;
    --dark-2: #2e2e2e;
    --panel: #f3f3f3;
  }
  * { box-sizing: border-box; margin: 0; padding: 0; }
  html, body { width: 1094px; height: 1200px; overflow: hidden; background: #fff; }
  body { position: relative; font-family: "Source Sans 3", Arial, sans-serif; color: var(--text); font-size: 11px; }
  .abs { position: absolute; }

  /* Header */
  .brand { left: 147px; top: 11px; width: 152px; height: 63px; }
  .brand-name { font-size: 21px; font-weight: 700; color: var(--orange); line-height: 1; margin-top: 6px; white-space: nowrap; }
  .brand-tag { font-size: 16px; color: var(--dark); margin-top: 8px; letter-spacing: .3px; }
  .cart { left: 852px; top: 10px; display: flex; align-items: center; gap: 6px; font-size: 12px; font-weight: 600; color: var(--dark); }
  .account-bar { left: 314px; top: 35px; width: 635px; height: 37px; background: linear-gradient(#fafafa, #ececec); border: 1px solid var(--line); border-radius: 2px; }
  .account-link { position: absolute; top: 0; height: 35px; line-height: 35px; font-size: 13px; color: var(--muted); text-align: center; border-right: 1px solid var(--line); }
  .search-input { left: 149px; top: 6px; width: 404px; height: 23px; background: #d4d4d4; border: 1px solid #c2c2c2; font-size: 11px; color: var(--muted); padding: 4px 8px; }
  .search-btn { left: 561px; top: 6px; width: 63px; height: 24px; background: linear-gradient(var(--orange-light), var(--orange)); color: #fff; font-size: 14px; text-align: center; line-height: 24px; }

  /* Navigation */
  .main-nav { left: 152px; top: 85px; width: 797px; height: 26px; background: linear-gradient(#2a2a2a, #050505); display: flex; }
  .main-nav a { color: #fff; text-decoration: none; font-size: 12px; line-height: 26px; text-align: center; border-right: 1px solid #555; }

  /* Hero */
  .hero { left: 152px; top: 119px; width: 798px; height: 261px; background: linear-gradient(90deg, #e6ebf0 0%, #cfd9e4 30%, #eef0f2 62%, #e9e9ea 100%); }
  .hero-shadow { left: 130px; top: 378px; width: 842px; height: 8px; background: radial-gradient(ellipse at center top, rgba(0,0,0,.25), rgba(0,0,0,0) 70%); }
  .hero-title { left: 688px; top: 182px; font-family: "Roboto Condensed", sans-serif; font-style: italic; font-weight: 700; color: var(--orange); font-size: 33px; line-height: 38px; }
  .hero-sub { left: 688px; top: 266px; font-family: "Roboto Condensed", sans-serif; font-style: italic; font-weight: 700; color: #333; font-size: 19px; line-height: 29px; }
  .hero-dots { left: 689px; top: 346px; display: flex; gap: 5px; }
  .hero-dots span { width: 10px; height: 10px; border-radius: 50%; background: #111; }
  .hero-dots span.active { background: var(--orange); }

  /* Section headers */
  .section-head { height: 29px; background: linear-gradient(var(--orange-light), var(--orange)); color: #fff; font-size: 15px; font-weight: 600; line-height: 29px; padding-left: 10px; }
  .head-arrows { position: absolute; right: 8px; top: 9px; display: flex; gap: 4px; }
  .head-arrows span { width: 11px; height: 11px; border-radius: 50%; background: #fff; position: relative; }

  /* Products */
  .product-frame { width: 154px; height: 125px; border: 1px solid var(--frame); background: #fff; padding: 5px; }
  .product-frame div { width: 100%; height: 100%; }
  .product-name { font-size: 11.5px; color: var(--text); white-space: nowrap; }
  .product-price { font-size: 11.5px; color: var(--red-price); }
  .vline { width: 1px; background: var(--line); }
  .hline { height: 1px; background: var(--line); }

  /* Readers */
  .reader-photo { width: 89px; height: 87px; }
  .reader-name { font-size: 11px; color: var(--orange); }
  .reader-text { font-size: 10.5px; line-height: 15px; color: var(--text); width: 134px; }
  .btn-grey { background: #d0d0d0; border: 1px solid #c4c4c4; color: var(--dark); font-size: 11px; text-align: center; line-height: 22px; }

  /* Marketplace */
  .market-img { width: 106px; height: 142px; }
  .market-name { font-size: 14px; color: var(--maroon); }
  .market-price { font-size: 12px; font-weight: 600; color: var(--orange); }

  /* Newsletter */
  .email-input { left: 714px; top: 977px; width: 235px; height: 30px; border: 1px solid var(--line); font-size: 10px; color: var(--muted); padding: 8px 13px; }
  .subscribe { left: 869px; top: 1017px; width: 80px; height: 28px; background: linear-gradient(var(--orange-light), var(--orange)); color: #fff; font-size: 15px; text-align: center; line-height: 28px; }

  /* Footer */
  .site-footer { left: 152px; top: 1058px; width: 797px; height: 138px; background: linear-gradient(var(--dark-2), var(--dark)); color: #fff; text-align: center; }
  .follow { top: 13px; width: 100%; font-size: 11px; }
  .social { top: 41px; left: 353px; display: flex; gap: 6px; }
  .social span { width: 19px; height: 19px; border-radius: 3px; background: #5b5b5b; }
  .footer-rule { top: 76px; left: 0; width: 100%; height: 1px; background: #444; }
  .footer-links { top: 90px; width: 100%; font-size: 11px; }
  .footer-links span.sep { margin: 0 5px; }
  .copyright { top: 109px; width: 100%; font-size: 11px; }
</style>
</head>
<body>

<header>
  <div class="abs brand">
    <div class="brand-name">Lantern of Seers</div>
    <div class="brand-tag">a world of psychics</div>
  </div>
  <div class="abs cart">
    <svg width="18" height="15" viewBox="0 0 18 15" aria-hidden="true"><path d="M1 5h16l-2 9H3z" fill="#222"/><path d="M5 5l4-4 4 4" fill="none" stroke="#222" stroke-width="1.5"/></svg>
    Shopping Cart
  </div>
  <div class="abs account-bar">
    <div class="account-link" style="left:0;width:72px;">Register</div>
    <div class="account-link" style="left:72px;width:68px;">Sign In</div>
    <div class="abs search-input">Search</div>
    <div class="abs search-btn">Search</div>
  </div>
  <nav class="abs main-nav">
    <a style="width:64px">Home</a>
    <a style="width:71px">Psychics</a>
    <a style="width:86px">Marketplace</a>
    <a style="width:99px">Psychic Profile</a>
    <a style="width:96px">Psychic Store</a>
    <a style="width:108px">Psychic Product</a>
  </nav>
</header>

<section>
  <div class="abs hero" role="img" aria-label="Photo of a smiling man using a laptop on a sofa"></div>
  <div class="abs hero-shadow"></div>
  <div class="abs hero-title">Welcome to<br>Our Site</div>
  <div class="abs hero-sub">The Best Psychics are here for you<br>try a live psychic reading today.</div>
  <div class="abs hero-dots"><span></span><span></span><span class="active"></span><span></span><span></span></div>
</section>

<main>
  <div class="abs section-head" style="left:152px;top:401px;width:548px;">Products</div>

  <div class="abs vline" style="left:329px;top:437px;height:569px;"></div>
  <div class="abs vline" style="left:526px;top:437px;height:569px;"></div>
  <div class="abs hline" style="left:153px;top:616px;width:546px;"></div>
  <div class="abs hline" style="left:153px;top:805px;width:546px;"></div>

  <!-- Row 1 -->
  <div class="abs product-frame" style="left:153px;top:440px;"><div role="img" aria-label="Rope-wrapped jar pendant lamps" style="background:linear-gradient(135deg,#8a7358,#3b2a1d 60%,#c9a36a);"></div></div>
  <div class="abs product-name" style="left:152px;top:573px;">Fines herbes - Aromatics Culina</div>
  <div class="abs product-price" style="left:152px;top:590px;">$39.00 USD</div>

  <div class="abs product-frame" style="left:348px;top:440px;"><div role="img" aria-label="Art print of a running rabbit" style="background:linear-gradient(135deg,#1a1a22,#e6e3dc 40%,#d9d2c2);"></div></div>
  <div class="abs product-name" style="left:347px;top:573px;">Art print - Run Rabbit - A5 digita</div>
  <div class="abs product-price" style="left:347px;top:590px;">$39.00 USD</div>

  <div class="abs product-frame" style="left:545px;top:440px;"><div role="img" aria-label="Wooden spoon with apples on linen" style="background:linear-gradient(135deg,#9fa39a,#6b6e68 50%,#3a3c3a);"></div></div>
  <div class="abs product-name" style="left:543px;top:573px;">Rustic Oversized Wooden Spoo</div>
  <div class="abs product-price" style="left:543px;top:590px;">$39.00 USD</div>

  <!-- Row 2 -->
  <div class="abs product-frame" style="left:153px;top:629px;"><div role="img" aria-label="White hen on black background" style="background:linear-gradient(90deg,#050505,#2a241c 50%,#0a0a0a);"></div></div>
  <div class="abs product-name" style="left:152px;top:762px;">Chicken Babies Room Kitchen Bird</div>
  <div class="abs product-price" style="left:152px;top:779px;">$39.00 USD</div>

  <div class="abs product-frame" style="left:348px;top:629px;"><div role="img" aria-label="Moss terrarium in a petri dish on books" style="background:linear-gradient(180deg,#c9ccc7,#4e6b2e 55%,#2a2f35);"></div></div>
  <div class="abs product-name" style="left:347px;top:762px;">Petri Dish Plant Terrarium - Sci</div>
  <div class="abs product-price" style="left:347px;top:779px;">$39.00 USD</div>

  <div class="abs product-frame" style="left:545px;top:629px;"><div role="img" aria-label="Striped cloth napkins with cutlery" style="background:linear-gradient(135deg,#6a6a6a,#bdbdbd 50%,#4a4a4a);"></div></div>
  <div class="abs product-name" style="left:543px;top:762px;">8 Organic Stripe Napkins - Org</div>
  <div class="abs product-price" style="left:543px;top:779px;">$39.00 USD</div>

  <!-- Row 3 -->
  <div class="abs product-frame" style="left:153px;top:820px;"><div role="img" aria-label="Small pottery salt cellar" style="background:linear-gradient(180deg,#5e5f61,#47484a 60%,#7b7b7b);"></div></div>
  <div class="abs product-name" style="left:152px;top:953px;">open salt cellar, pottery dish. brow</div>
  <div class="abs product-price" style="left:152px;top:970px;">$39.00 USD</div>

  <div class="abs product-frame" style="left:348px;top:820px;"><div role="img" aria-label="Hanging memo chalkboards" style="background:linear-gradient(135deg,#5a5d61,#2b2f35 50%,#6b6e72);"></div></div>
  <div class="abs product-name" style="left:347px;top:953px;">Hanging Memo Chalkboard</div>
  <div class="abs product-price" style="left:347px;top:970px;">$39.00 USD</div>

  <div class="abs product-frame" style="left:545px;top:820px;"><div role="img" aria-label="Wire basket filled with eggs" style="background:radial-gradient(circle,#cfc7bd,#6f6c68 55%,#3f3d3b);"></div></div>
  <div class="abs product-name" style="left:543px;top:953px;">Vintage Wire Egg Basket, rusti</div>
  <div class="abs product-price" style="left:543px;top:970px;">$39.00 USD</div>
</main>

<aside>
  <div class="abs section-head" style="left:714px;top:401px;width:235px;">Top Psychic Readers
    <div class="head-arrows"><span></span><span></span></div>
  </div>
  <div class="abs reader-photo" role="img" aria-label="Portrait of psychic reader Ravin" style="left:716px;top:441px;background:linear-gradient(135deg,#6b4a3a,#b78a72 50%,#d6c0d8);"></div>
  <div class="abs reader-name" style="left:815px;top:442px;">Ravin</div>
  <div class="abs reader-text" style="left:815px;top:455px;">A study attempted to repeat recently reported parapsy-chological experiments that appeared to support the existence.</div>
  <div class="abs hline" style="left:716px;top:541px;width:235px;"></div>
  <div class="abs reader-photo" role="img" aria-label="Portrait of two psychic readers outdoors" style="left:716px;top:554px;background:linear-gradient(135deg,#3d5a2a,#8a7a6a 50%,#2a3a4a);"></div>
  <div class="abs reader-name" style="left:815px;top:555px;">Psychic</div>
  <div class="abs reader-text" style="left:815px;top:568px;">My Expert Service Hello! I am a gifted seer and psychic blessed to empower people with life's truths and - See more at:</div>
  <div class="abs btn-grey" style="left:859px;top:650px;width:92px;height:24px;">Read More All</div>

  <div class="abs section-head" style="left:714px;top:693px;width:235px;">Marketplace
    <div class="head-arrows"><span></span><span></span></div>
  </div>
  <div class="abs market-img" role="img" aria-label="Love spells heart artwork" style="left:716px;top:730px;background:radial-gradient(circle,#f2d6d6,#b01418 45%,#3a0608);"></div>
  <div class="abs market-name" style="left:715px;top:880px;">Love Spell</div>
  <div class="abs market-price" style="left:715px;top:899px;">Price: $200.00</div>
  <div class="abs market-img" role="img" aria-label="Lit white candle with ornaments" style="left:840px;top:730px;background:radial-gradient(circle at 50% 40%,#f4ead2,#3a3a3a 40%,#0a0a0a);"></div>
  <div class="abs market-name" style="left:839px;top:880px;">Candle</div>
  <div class="abs market-price" style="left:839px;top:899px;">Price: $12.00</div>

  <div class="abs section-head" style="left:714px;top:937px;width:235px;">Newsletter Signup</div>
  <div class="abs email-input">Enter the Email id</div>
  <div class="abs subscribe">Subscribe</div>
</aside>

<footer class="abs site-footer">
  <div class="abs follow">Follow us On</div>
  <div class="abs social" aria-label="Social links"><span></span><span></span><span></span><span></span></div>
  <div class="abs footer-rule"></div>
  <div class="abs footer-links">Home<span class="sep">|</span>Psychic<span class="sep">|</span>Marketplace<span class="sep">|</span>Psychic profile page<span class="sep">|</span>Psychic Store page<span class="sep">|</span>Psychic product page<span class="sep">|</span></div>
  <div class="abs copyright">Copyrights @ 2013 All Rights Reserved</div>
</footer>

</body>
</html>
```